Training company needs a Quick Reference Card design

We have draft skeleton of the design and most of the text. But we need a designer to take it the rest if the way.
I have designed a 2 page quick reference card - it is meant to be a 2-sided document. The first page is portrait, the back page can either be portrait or landscape, I'm not too concerned, whichever fits best.
Section called 'Maps' on front, a map is a collection of documents (like a manual), a topic is a document (like a page or section of a manual) and a block is a section of a document. The graphic is mean to illustrate the hierarchy but essentially a map is a big document with smaller documents in it.
Please use the company's logo colors to differentiate the different sections with minimal/ highlight only use of the darkest color, preferably.
Please use the icons for the corresponding Information types in the chart of the back - except please re-design the icons color scheme to match the company's logo/website colors.

Target Market(s)

Technical writers, after attending our training course, as an ongoing resource for them

Industry/Entity Type

It Company

Font styles to use
Sans Serif

Requirements
Must have
• Must adhere to look and feel of brand/ website. www.lumarockwise.com
Nice to have
• Please keep the design modern and slick looking, not too busy, easy to read

```html
<!DOCTYPE html>
<html lang="en">
<head>
<meta charset="utf-8">
<title>Quick Reference Card</title>
<link href="https://fonts.googleapis.com/css2?family=Roboto+Condensed:wght@300;400;700&display=swap" rel="stylesheet">
<style>
:root{
  --navy:#2b2f8f;
  --blue:#14a0d9;
  --sky:#c9e9f6;
  --slate:#86b3c3;
  --mid:#5fb2e2;
  --pale:#9dcdea;
  --table:#7fbfe5;
  --table-head:#a9d4ee;
  --ink:#1d2a3a;
  --white:#ffffff;
}
*{box-sizing:border-box;margin:0;padding:0}
html,body{width:1200px;height:1200px;overflow:hidden;background:#fff}
body{position:relative;font-family:"Roboto Condensed",sans-serif;color:var(--ink)}
.abs{position:absolute}

/* brand */
.brand{left:42px;top:242px;display:flex;align-items:center;gap:6px}
.brand-dot{width:40px;height:40px;border-radius:50%;background:var(--blue)}
.brand-name{font-weight:700;font-size:15px;color:var(--navy);letter-spacing:.2px}

.title-bar-top{left:294px;top:232px;width:273px;height:6px;background:var(--navy)}
.title-pill{left:218px;top:242px;width:349px;height:34px;background:var(--blue);border-radius:17px 0 0 17px;color:#fff;
  font-weight:700;font-size:28px;font-variant:small-caps;letter-spacing:1px;line-height:34px;text-align:center}
.title-bar-bottom{left:386px;top:282px;width:181px;height:6px;background:var(--blue)}

.topic-quote{left:92px;top:300px;width:420px;font-size:14px;font-variant:small-caps;letter-spacing:.6px;line-height:22px;color:var(--ink)}
.topic-quote b{color:var(--navy);font-size:18px}

/* map */
.map{left:42px;top:353px;width:308px;height:181px;background:var(--blue);color:#fff;font-size:11px}
.map-label{position:absolute;top:8px;width:100%;text-align:center}
.map-inner{position:absolute;left:14px;top:29px;width:149px;height:136px;background:var(--sky);color:var(--blue)}
.map span{position:absolute;width:149px;text-align:center}
.note{font-size:10.5px;line-height:13.5px;padding:4px 5px;color:#fff}
.note-map{left:358px;top:353px;width:209px;height:58px;background:var(--blue)}
.note-topic{left:358px;top:421px;width:209px;height:43px;background:var(--sky);color:var(--slate)}
.note-block{left:358px;top:474px;width:209px;height:60px;background:var(--slate)}

/* rules */
.rules{left:24px;top:544px;width:543px;height:110px;background:var(--sky)}
.rules-title{left:24px;top:548px;width:543px;text-align:center;font-size:11.5px;color:var(--blue)}
.rule{top:566px;height:108px;background:var(--slate);color:#fff;font-size:10.5px;line-height:13.6px;text-align:center;padding:6px 5px}
.rule h3,.principle h3{font-size:11px;font-weight:700}

.questions{font-size:10.5px;line-height:13.6px;color:var(--mid)}
.questions h4{font-weight:700;color:var(--slate);font-size:10.5px}
.questions ol{list-style:none}

.principles-title{left:42px;top:780px;width:508px;text-align:center;font-weight:700;font-size:11px;color:var(--blue)}
.principle{top:802px;width:116px;height:108px;color:#fff;font-size:10.5px;line-height:13.6px;text-align:center;padding:5px 4px}

/* info types table */
.types{left:674px;top:292px;width:438px;height:616px;border-collapse:collapse;background:var(--table);
  font-size:8.3px;line-height:12.4px;color:#2a3440;table-layout:fixed}
.types th,.types td{border-top:2px solid #b9dcf1;padding:3px 4px;vertical-align:middle;text-align:left;font-weight:400}
.types thead th{background:var(--table-head);text-align:center;letter-spacing:.3px;border-top:none}
.types tbody th{text-align:center;font-size:8.8px;letter-spacing:.3px}
</style>
</head>
<body>

<div class="abs brand"><div class="brand-dot"></div><div class="brand-name">LUMAROCKWISE.com</div></div>
<div class="abs title-bar-top"></div>
<div class="abs title-pill">Quick Reference Card</div>
<div class="abs title-bar-bottom"></div>

<p class="abs topic-quote"><b>“</b>Topic: Neque porro quisquam est qui dolorem ipsum quia dolor sit amet, consectetur, adipisci velit... <b>”</b></p>

<div class="abs map">
  <div class="map-label">MAP</div>
  <div class="map-inner">
    <span style="top:30px">Primary Block</span>
    <span style="top:88px">Sub Block</span>
  </div>
  <span style="left:154px;top:38px;line-height:14px">TOPIC<br>Primary Block</span>
  <span style="left:154px;top:118px">Sub Block</span>
</div>
<div class="abs note note-map">A map is a file that organizes topics into structured collections of information. Maps specify hierarchy and relationships among topics.</div>
<div class="abs note note-topic">A topic is a group of related blocks with a title. Use the chunking principle to group together relevant blocks.</div>
<div class="abs note note-block">A block is a bite-sized chunk of information about one main idea that allows the writer to organize the material into logical sections.</div>

<div class="abs rules"></div>
<div class="abs rules-title">GENERAL WRITING RULES</div>
<div class="abs rule" style="left:64px;width:148px"><h3>Effective sentences</h3>One main agent, action &amp; outcome. Use active voice and simplest tense possible. No more than 7 sentences per paragraph. Use lists and tables.</div>
<div class="abs rule" style="left:220px;width:150px"><h3>Special characters</h3>Avoid special characters, spell out words instead. Remove parentheses, colons and dashes. Avoid using quotation marks and slashes.</div>
<div class="abs rule" style="left:378px;width:149px"><h3>Plain language</h3>Write in short sentences. Provide useful titles. Use clear familiar words. Avoid excess words. Be consistent.</div>

<div class="abs questions" style="left:42px;top:698px;width:240px">
  <h4>3 Questions to ask before you start writing:</h4>
  <ol><li>1. What is the purpose of this information?</li>
  <li>2. What is the desired user response of this<br>&nbsp;&nbsp;&nbsp;&nbsp;information?</li>
  <li>3. Who is the audience?</li></ol>
</div>
<div class="abs questions" style="left:334px;top:698px;width:230px">
  <h4>2 Types of language arts</h4>
  <p>LAFI – Language arts for information</p>
  <p>LAFPR – language arts for personal response</p>
</div>

<div class="abs principles-title">4 Cognitive Principles</div>
<div class="abs principle" style="left:64px;background:var(--blue)"><h3>Consistency</h3>Use similar terms and structures. Pick a term and stick with it. Use the same sequence of blocks. Use consistent styles.</div>
<div class="abs principle" style="left:180px;background:var(--mid)"><h3>Chunking</h3>Maximum of nine (7 +/- 2) items in a list, rows in a table, blocks in a topic, or topics in a map.</div>
<div class="abs principle" style="left:296px;background:#7dbde6"><h3>Relevance</h3>Group similar items together. Separate relevance? Separate block. Irrelevant? Delete it.</div>
<div class="abs principle" style="left:411px;background:var(--pale)"><h3>Titling</h3>Name everything. Name every block, every topic, every map and every table column.</div>

<table class="abs types">
  <colgroup><col style="width:74px"><col><col><col><col><col></colgroup>
  <thead><tr style="height:74px"><th></th><th>REFERENCE</th><th>CONCEPT</th><th>PRINCIPLE</th><th>PROCESS</th><th>TASK</th></tr></thead>
  <tbody>
    <tr style="height:74px"><th>DEFINITION</th>
      <td>Describes things the reader needs to know</td><td>Explains things the reader needs to understand</td><td>Advises the reader what they need to do or not do and when</td><td>Demonstrates to the reader how things work</td><td>Instructs the reader on how to do things</td></tr>
    <tr style="height:134px"><th>TYPES OF AUTHORING MODELS</th>
      <td>Sentences / phrases<br>Lists (ol, ul)<br>Tables<br>Diagrams<br>Part-description<br>Part-function</td>
      <td>Sentences/phrases<br>Lists (ol, ul)<br>Tables<br>Illustrations</td>
      <td>Sentences/phrases<br>Lists (ol, ul)<br>Tables<br>Decision tree<br>Graphic</td>
      <td>Sentences/phrases<br>Stage ordered list<br>When/then condition tree<br>Graphic example</td>
      <td>Sentences/phrases<br>Lists<br>If/then decision tree<br>Graphic example</td></tr>
    <tr style="height:146px"><th>TITLING BEST PRACTICES</th>
      <td>Describes the item and anything that differentiates it from other items</td>
      <td>Use the plural form of the noun, if one exists. Don't add additional words such as “About”, “What is”, or “Definition”</td>
      <td>Identifies the principle and expresses the gravity of the principle. Formula= gravity + principle, or principle + gravity</td>
      <td style="line-height:11px">Human processes: Gerund of verb + noun “Grooming a dog”. System processes: Use “How (item) works” Ex “How engines work”</td>
      <td style="line-height:11px">Starts with an imperative verb, do not use gerund. “Mow the lawn” “Boil and egg” “Register for a course”</td></tr>
    <tr style="height:37px"><th>PRIMARY BLOCK TITLE</th>
      <td>Introduction</td><td>Definition</td><td>Statement</td><td>Summary</td><td>Purpose</td></tr>
    <tr style="height:107px"><th>PRIMARY BLOCK CONTENT</th>
      <td>Provide a description of the reference topic and how it would be used</td>
      <td>Provide the exact meaning of the concept</td>
      <td>Provide a high-level summary of the principle</td>
      <td>Provide a short explanation of the purpose of the process, or the need for the process</td>
      <td>Provide an explanation of why or when the reader would use the task</td></tr>
    <tr style="height:44px"><th>TIPS AND EXAMPLES</th><td></td><td></td><td></td><td></td><td></td></tr>
  </tbody>
</table>

</body>
</html>
```